We need (2) 4"X4" product label designs for the front and back of an RTU hose on bottle (see attached examples) for a brand new, first-of-its-kind, Aloe Vera product (VerdaKin "The Supreme Root Tonic") specially formulated for agriculture. Most people are aware of the medicinal benefits of aloe vera, however, most people are unaware that it can be used as a soil amendment (organic fertilizer) for plants and lawns, as well as many other crops. This product is for the consumer market. There are about 15 elements that need to go on the front label (which I will provide moving forward), and the backside provides instructions and other relevant information about the product. I will provide a range of examples on the next step of this project.

Need extra days to review

```html
<!DOCTYPE html>
<html lang="en">
<head>
<meta charset="utf-8">
<title>VerdaKin – The Supreme Root Tonic</title>
<link rel="stylesheet" href="https://fonts.googleapis.com/css2?family=Jost:wght@300;400;500&display=swap">
<style>
  :root {
    --mint: #dff0e1;
    --leaf: #246641;
    --leaf-soft: #3f8259;
    --ink: #111111;
  }
  html, body {
    margin: 0;
    padding: 0;
    overflow: hidden;
    background: var(--mint);
  }
  .label {
    position: relative;
    width: 1200px;
    height: 1200px;
    overflow: hidden;
    background: var(--mint);
    font-family: "Jost", sans-serif;
  }
  .brand-name {
    position: absolute;
    top: 92px;
    left: 0;
    width: 1200px;
    margin: 0;
    text-align: center;
    font-family: "Jost", sans-serif;
    font-weight: 500;
    font-size: 176px;
    line-height: 1;
    letter-spacing: -2px;
    color: var(--leaf);
  }
  .tagline {
    position: absolute;
    top: 352px;
    left: 0;
    width: 1200px;
    margin: 0;
    text-align: center;
    font-family: "Jost", sans-serif;
    font-weight: 300;
    font-size: 50px;
    line-height: 1.2;
    color: var(--ink);
  }
  .descriptor {
    position: absolute;
    top: 432px;
    left: 0;
    width: 1200px;
    margin: 0;
    text-align: center;
    font-family: "Jost", sans-serif;
    font-weight: 300;
    font-size: 35px;
    line-height: 44px;
    letter-spacing: 0.5px;
    color: var(--leaf);
  }
  .aloe-art {
    position: absolute;
    background: radial-gradient(ellipse at 50% 100%, var(--leaf) 0%, var(--leaf) 45%, var(--leaf-soft) 75%, rgba(63,130,89,0) 100%);
  }
  .aloe-art--main {
    left: 47px;
    top: 528px;
    width: 723px;
    height: 624px;
    border-radius: 50% 50% 30% 30% / 80% 80% 20% 20%;
  }
  .aloe-art--corner {
    left: 984px;
    top: 862px;
    width: 260px;
    height: 320px;
    border-radius: 50% 50% 30% 30% / 80% 80% 20% 20%;
  }
</style>
</head>
<body>
  <main class="label">
    <h1 class="brand-name">VerdaKin</h1>
    <p class="tagline">The Supreme Root Tonic</p>
    <p class="descriptor">organic fertilizer<br>for plants and lawns</p>
    <div class="aloe-art aloe-art--main" role="img" aria-label="Line-and-fill illustration of a large aloe vera plant with long pointed green leaves"></div>
    <div class="aloe-art aloe-art--corner" role="img" aria-label="Illustration of a small aloe vera plant partly cut off at the lower right corner"></div>
  </main>
</body>
</html>
```